依頼詳細
レスポンシブウェブデザインを意識したデザインでお願いします。

デザインに関しては、添付してあるデザインレイアウトシートを基にお願いします。
参考サイトのURLはデザインレイアウトシートに記載してあります。
色合いはグリーンかブルーを基調にお願いします。
新規のウェブサイトですので、既存サイトはありません。
ロゴも不要です。(後ではめ込むので社名だけテキストでレイアウトをお願いします。)
また、写真データも添付するので、レイアウトシートのイメージ画像に当て込んでください。

まずはパソコンサイトのデザインをお願いします。
当選後、スマホデザインをお願いします。

既存のテンプレートを使う場合は
テンプレート名を下記のような記載を提案の中にいれてください。
例:WordpressテーマはCorpLumen、デザインスキンは無料のQRN2019 LX4(http://corplumen.example/ex_plugin/qrnfuji2019_lx4/)をベースにデザインいたしました。
など

写真データで足りない場合は、一旦他のサイトや参考URLの写真をサンプルとして入れてください。(サンプルなどの表記をお願いします)
また、購入が必要な写真などを利用した場合は、Pixora Stock(https://stock.pixora-img.example/jp/)からファイル番号と価格を教えてください。
ページ数
1ページ
希望イメージ
シンプル 複雑
単色 カラフル
暗い 明るい
日常 高級
遊び心 厳粛
未来的 伝統的
女性的 男性的
希望する色
青系、緑系
納品ファイル
• イラストレーター形式 (.ai)
• フォトショップ形式 (.psd)
• PNG形式 (.png)
補足説明
上記のいずれか1つ。アウトラインありとなしの2つ。

こちらの要望を汲んで、デザインしていただきました。
ありがとうございました。

たくさんのご提案ありがとうございました。
次回もぜひ、よろしくお願い致します。

```html
<!DOCTYPE html>
<html lang="ja">
<head>
<meta charset="UTF-8">
<title>有限会社青嶺</title>
<link href="https://fonts.googleapis.com/css2?family=Noto+Sans+JP:wght@400;500;700&family=Montserrat:wght@500;600&display=swap" rel="stylesheet">
<style>
:root{
  --blue:#1f6db3;
  --blue-dark:#174f85;
  --sky:#dce9f6;
  --teal:#2ba6c9;
  --teal-pale:#cde9f2;
  --ink:#222;
  --muted:#666;
  --line:#dcdcdc;
  --footer:#555;
  --orange:#e58a2e;
}
*{margin:0;padding:0;box-sizing:border-box}
html,body{width:1200px;height:4332px;overflow:hidden}
body{position:relative;background:#fff;color:var(--ink);font-family:"Noto Sans JP",sans-serif}
.abs{position:absolute}
.label{font-family:"Montserrat",sans-serif;font-size:11px;letter-spacing:.15em;color:var(--blue);font-weight:600}
.heading{font-size:26px;font-weight:700;letter-spacing:.08em}
.body-text{font-size:13px;line-height:2.1;letter-spacing:.12em;color:#444}
.btn{display:flex;align-items:center;justify-content:center;background:var(--blue);color:#fff;font-size:13px;letter-spacing:.08em;height:44px}
.btn::after{content:"›";margin-left:22px;font-size:16px}
/* header / hero */
.hero{left:0;top:0;width:1200px;height:752px;background:linear-gradient(180deg,#1b2c44 0%,#35577f 45%,#8aa3bf 70%,#2b3645 100%)}
.site-name{left:28px;top:18px;color:#fff;font-size:22px;font-weight:700;letter-spacing:.05em}
.global-nav{right:26px;top:22px;display:flex;gap:30px;color:#fff;font-size:13px}
.hero-copy{left:0;width:1200px;top:352px;text-align:center;color:#fff;font-size:38px;font-weight:700;letter-spacing:.12em}
.scroll{left:0;width:1200px;top:650px;text-align:center;color:#fff;font-family:"Montserrat",sans-serif;font-size:11px;letter-spacing:.2em}
.scroll::after{content:"";display:block;width:1px;height:60px;background:#fff;margin:10px auto 0}
/* about */
.about-band{left:0;top:800px;width:720px;height:500px;background:var(--sky)}
.about-photo{left:100px;top:840px;width:600px;height:420px;background:linear-gradient(135deg,#7f8fa3,#b7c3cf 50%,#5c6a7b)}
/* services */
.service-grid{left:0;top:1568px;width:1200px;height:480px;display:grid;grid-template-columns:repeat(3,400px);grid-template-rows:repeat(2,240px)}
.service-card{position:relative;background:linear-gradient(135deg,#3f4954,#6c7783);color:#fff;border:1px solid rgba(255,255,255,.2)}
.service-card:nth-child(2n){background:linear-gradient(135deg,#4c5a68,#8593a1)}
.service-card h3{position:absolute;left:0;width:100%;top:92px;text-align:center;font-size:16px;font-weight:500;letter-spacing:.1em}
.service-card p{position:absolute;left:0;width:100%;top:124px;text-align:center;font-size:11px;letter-spacing:.08em;line-height:1.8}
.service-card .arrow{position:absolute;right:0;bottom:0;width:26px;height:26px;background:var(--blue);color:#fff;display:flex;align-items:center;justify-content:center;font-size:14px}
/* recruit */
.recruit-tab{left:100px;top:2180px;width:280px;height:132px;background:var(--teal);color:#fff;padding:36px 32px}
.recruit-tab .label{color:#fff}
.recruit-band{left:180px;top:2352px;width:920px;height:336px;background:var(--teal-pale)}
.recruit-photo{left:180px;top:2360px;width:840px;height:320px;background:linear-gradient(120deg,#c6ccd1,#eef0f2 45%,#9aa4ad)}
.recruit-catch{left:180px;width:840px;top:2524px;text-align:center;color:#fff;font-size:18px;font-weight:700;letter-spacing:.1em;text-shadow:0 1px 3px rgba(0,0,0,.3)}
/* news */
.divider{left:100px;top:2760px;width:1000px;height:1px;background:var(--line)}
.news-list{left:180px;top:2912px;width:840px}
.news-item{display:flex;align-items:center;height:64px;border-bottom:1px solid var(--line);font-size:12px;letter-spacing:.08em}
.news-item time{width:100px;color:var(--blue);font-family:"Montserrat",sans-serif;font-weight:500}
.tag{width:72px;height:20px;color:#fff;font-size:11px;display:flex;align-items:center;justify-content:center;margin-right:24px}
/* contact */
.contact{left:100px;top:3260px;width:1000px;height:300px;background:linear-gradient(135deg,#e4e8ec,#cfd6dd);text-align:center}
.contact-btn{left:520px;top:3410px;width:200px;height:44px;background:#222;color:#fff;font-size:13px;display:flex;align-items:center;justify-content:center;gap:10px}
.contact-tel{left:0;width:1200px;top:3476px;text-align:center;color:var(--blue);font-family:"Montserrat",sans-serif;font-size:30px;font-weight:600;letter-spacing:.04em}
/* map & footer */
.map{left:0;top:3600px;width:1200px;height:472px;background:linear-gradient(160deg,#e9e9e7,#d8dbd6 60%,#e4e2dc)}
.to-top{left:1140px;top:4020px;width:44px;height:44px;border-radius:50%;background:var(--blue);color:#fff;display:flex;align-items:center;justify-content:center;font-size:16px}
.footer{left:0;top:4072px;width:1200px;height:260px;background:var(--footer);color:#fff;text-align:center}
.footer-nav{display:flex;justify-content:center;gap:48px;font-size:12px;padding-top:40px}
.footer-name{font-size:18px;font-weight:700;margin-top:32px;letter-spacing:.05em}
.footer-addr{font-size:11px;margin-top:10px;color:#eee}
.footer-sub{font-size:11px;margin-top:12px;color:#ddd}
.copyright{font-family:"Montserrat",sans-serif;font-size:10px;margin-top:16px;color:#ccc}
</style>
</head>
<body>

<section class="abs hero" role="img" aria-label="足場に立つ作業員のシルエットと青空の写真"></section>
<div class="abs site-name">有限会社青嶺</div>
<nav class="abs global-nav"><span>ホーム</span><span>お知らせ</span><span>会社案内</span><span>業務内容</span><span>採用情報</span><span>お問い合わせ</span></nav>
<h1 class="abs hero-copy">建設現場の安全と快適を支えます。</h1>
<div class="abs scroll">SCROLL</div>

<div class="abs about-band"></div>
<div class="abs about-photo" role="img" aria-label="倉庫で足場資材を整備する作業員の写真"></div>
<div class="abs label" style="left:880px;top:860px">ABOUT</div>
<h2 class="abs heading" style="left:880px;top:890px">当社の特徴</h2>
<p class="abs body-text" style="left:880px;top:950px;width:280px">テキストテキストテキストテキストテキストテキストテキストテキストテキストテキストテキストテキストテキストテキストテキストテキストテキストテキストテキストテキストテキストテキストテキストテキストテキスト</p>
<div class="abs btn" style="left:820px;top:1188px;width:220px">当社の特徴を見る</div>

<div class="abs label" style="left:0;width:1200px;text-align:center;top:1384px">BUSINESS</div>
<h2 class="abs heading" style="left:0;width:1200px;text-align:center;top:1410px">業務内容</h2>
<p class="abs body-text" style="left:310px;top:1468px;width:600px">テキストテキストテキストテキストテキストテキストテキストテキストテキストテキストテキストテキストテキストテキストテキストテキストテキストテキストテキストテキスト</p>
<div class="abs service-grid">
  <div class="service-card" role="img" aria-label="積み上げられた足場資材の写真"><h3>タイトル</h3><p>テキストテキストテキストテキスト<br>テキストテキストテキスト</p><span class="arrow">›</span></div>
  <div class="service-card" role="img" aria-label="資材倉庫内の写真"><h3>タイトル</h3><p>テキストテキストテキストテキスト<br>テキストテキストテキスト</p><span class="arrow">›</span></div>
  <div class="service-card" role="img" aria-label="倉庫で作業する様子の写真"><h3>タイトル</h3><p>テキストテキストテキストテキスト<br>テキストテキストテキスト</p><span class="arrow">›</span></div>
  <div class="service-card" role="img" aria-label="資材を運ぶ作業員の写真"><h3>タイトル</h3><p>テキストテキストテキストテキスト<br>テキストテキストテキスト</p><span class="arrow">›</span></div>
  <div class="service-card" role="img" aria-label="並べられた鋼管の写真"><h3>タイトル</h3><p>テキストテキストテキストテキスト<br>テキストテキストテキスト</p><span class="arrow">›</span></div>
  <div class="service-card" role="img" aria-label="屋内の資材置き場の写真"><h3>タイトル</h3><p>テキストテキストテキストテキスト<br>テキストテキストテキスト</p><span class="arrow">›</span></div>
</div>

<div class="abs recruit-tab"><div class="label">RECRUIT</div><div class="heading" style="font-size:24px;margin-top:6px">採用情報</div></div>
<p class="abs body-text" style="left:410px;top:2184px;width:690px">テキストテキストテキストテキストテキストテキストテキストテキストテキストテキストテキストテキストテキストテキストテキストテキストテキストテキストテキストテキストテキストテキストテキストテキストテキストテキスト</p>
<div class="abs recruit-band"></div>
<div class="abs recruit-photo" role="img" aria-label="ヘルメット姿の作業員二人が資材を扱う写真"></div>
<div class="abs recruit-catch">一緒に、未来を切り開いていきませんか</div>
<div class="abs btn" style="left:490px;top:2600px;width:220px">採用情報はこちら</div>

<div class="abs divider"></div>
<div class="abs label" style="left:0;width:1200px;text-align:center;top:2836px">NEWS</div>
<h2 class="abs heading" style="left:0;width:1200px;text-align:center;top:2860px">お知らせ</h2>
<div class="abs news-list">
  <div class="news-item"><time>2020.00.00</time><span class="tag" style="background:var(--blue)">お知らせ</span><span>テキストテキストテキストテキストテキストテキストテキストテキストテキスト</span></div>
  <div class="news-item"><time>2020.00.00</time><span class="tag" style="background:var(--teal)">採用情報</span><span>テキストテキストテキストテキストテキストテキストテキストテキストテキスト</span></div>
  <div class="news-item"><time>2020.00.00</time><span class="tag" style="background:var(--orange)">業務内容</span><span>テキストテキストテキストテキストテキストテキストテキストテキストテキスト</span></div>
</div>
<div class="abs btn" style="left:480px;top:3140px;width:240px">一覧を見る</div>

<div class="abs contact" role="img" aria-label="足場資材の写真を淡く敷いた背景"></div>
<div class="abs label" style="left:0;width:1200px;text-align:center;top:3300px">CONTACT</div>
<div class="abs" style="left:0;width:1200px;text-align:center;top:3344px;font-size:18px;font-weight:700;letter-spacing:.06em">ご質問など、お気軽にお問い合わせください</div>
<div class="abs contact-btn" style="left:500px">
  <svg width="16" height="12" viewBox="0 0 16 12"><rect x="0.5" y="0.5" width="15" height="11" fill="none" stroke="#fff"/><path d="M1 1l7 6 7-6" fill="none" stroke="#fff"/></svg>お問い合わせ</div>
<div class="abs contact-tel">
  <svg width="24" height="24" viewBox="0 0 24 24" style="vertical-align:-3px;margin-right:6px"><path fill="currentColor" d="M6.6 10.8a15.1 15.1 0 006.6 6.6l2.2-2.2c.3-.3.7-.4 1-.2 1.1.4 2.3.6 3.6.6.6 0 1 .4 1 1V20c0 .6-.4 1-1 1A17 17 0 013 4c0-.6.4-1 1-1h3.5c.6 0 1 .4 1 1 0 1.3.2 2.5.6 3.6.1.3 0 .7-.2 1z"/></svg>025-555-0184</div>

<div class="abs map" role="img" aria-label="所在地を示す地図"></div>
<div class="abs to-top">︿</div>
<footer class="abs footer">
  <nav class="footer-nav"><span>ホーム</span><span>お知らせ</span><span>会社案内</span><span>業務内容</span><span>採用情報</span><span>お問い合わせ</span></nav>
  <div class="footer-name">有限会社青嶺</div>
  <div class="footer-addr">〒000-0000 新潟県青嶺市中央町1-2-3　TEL：025-555-0184</div>
  <div class="footer-sub">個人情報保護方針　｜　サイトマップ</div>
  <div class="copyright">© Seirei Co., Ltd. All rights reserved.</div>
</footer>

</body>
</html>
```